Zielgruppe
Wir machen individualisierte Biere mit entsprechend coolen Etiketten-Designs. In diesem Fall ist es ein Geschenk für einen Freund, der heiratet.
Aufgabenstellung
Er hat seiner Verlobten den Heiratsantrag unter Polarlichtern in Island gemacht. Es wäre cool, wenn man karrikativ zwei Menschen, die Hände halten unter Polarlichtern sieht und der oben genannte Name 'Drevic' auf Kyrillisch (serb. für Liebe) in den Polarlichtern integriert ist. Ich habe unten als Inspiration die Webseite der Bierbrauerei angegeben, dort seht ihr den Stil der anderen Designs. Das Etiketten-Format findet ihr im Anhang. Im Anhang findet ihr auch ein Bild von den Polarlichtern, wo er ihr den Heiratsantrag gemacht hat, vielleicht hilft es euch zur Vorstellung.
Website: https://vornelo.rs/shop/

```html
<!DOCTYPE html>
<html lang="sr">
<head>
<meta charset="utf-8">
<title>Drevic – beer label</title>
<link href="https://fonts.googleapis.com/css2?family=Jost:wght@300;400;500&family=Space+Mono:wght@700&family=Comfortaa:wght@600&display=swap" rel="stylesheet">
<style>
  :root{
    --paper:#ffffff;
    --ink:#111111;
    --accent-red:#e5202a;
    --crop:#3a3a3a;
    --sky-night:#1c1a3a;
    --aurora-red:#f0545a;
    --aurora-orange:#f7a35c;
    --aurora-yellow:#f3e46a;
    --aurora-green:#6fc28a;
    --forest:#2f6f7a;
    --snow-pink:#f3b8cf;
    --snow-violet:#6b3c82;
  }
  html,body{margin:0;padding:0;overflow:hidden;background:var(--paper);}
  .label{position:relative;width:732px;height:1200px;background:var(--paper);overflow:hidden;font-family:"Jost",sans-serif;color:var(--ink);}
  .crop-marks{position:absolute;inset:0;}
  .volume-top{position:absolute;top:186px;left:0;width:732px;text-align:center;font-size:46px;font-weight:400;color:var(--accent-red);letter-spacing:1px;}
  .brand{position:absolute;top:300px;left:206px;width:332px;text-align:center;font-family:"Space Mono",monospace;font-weight:700;font-size:56px;letter-spacing:11px;line-height:62px;padding-left:11px;box-sizing:border-box;}
  .artwork{position:absolute;left:208px;top:369px;width:328px;height:434px;overflow:hidden;
    background:
      radial-gradient(ellipse 60% 30% at 50% 95%, var(--snow-violet), transparent 70%),
      radial-gradient(ellipse 90% 35% at 50% 88%, var(--snow-pink), transparent 75%),
      radial-gradient(ellipse 40% 30% at 55% 55%, #fff6d8, transparent 70%),
      linear-gradient(180deg, transparent 45%, rgba(47,111,122,.55) 65%, transparent 80%),
      radial-gradient(circle at 50% 62%, var(--aurora-yellow) 0 22%, var(--aurora-green) 34%, var(--aurora-orange) 44%, var(--aurora-red) 54%, var(--sky-night) 64%);
  }
  .artwork-title{position:absolute;left:0;top:88px;width:100%;text-align:center;font-family:"Comfortaa",sans-serif;font-weight:600;font-size:74px;line-height:1;color:#fff;letter-spacing:-1px;}
  .beer-name{position:absolute;top:812px;left:0;width:732px;text-align:center;font-size:34px;font-weight:400;letter-spacing:1px;}
  .vertical{position:absolute;transform:rotate(-90deg);transform-origin:center;white-space:nowrap;font-weight:300;font-size:16px;line-height:27px;text-align:center;}
  .description{left:-40px;top:517px;width:400px;height:54px;}
  .net{left:517px;top:433px;width:120px;}
  .abv{left:527px;top:733px;width:100px;}
  .signature-box{position:absolute;left:563px;top:552px;width:32px;height:98px;border:1px solid var(--accent-red);box-sizing:border-box;}
  .signature-box span{position:absolute;left:50%;top:50%;transform:translate(-50%,-50%) rotate(-90deg);white-space:nowrap;font-size:7px;line-height:9px;text-align:center;color:var(--accent-red);font-weight:500;}
  .dim{position:absolute;color:var(--accent-red);font-size:16px;font-weight:400;white-space:nowrap;}
  .dim-width{left:555px;top:528px;}
  .dim-height{left:577px;top:590px;width:50px;transform:rotate(-90deg);text-align:center;}
</style>
</head>
<body>
<div class="label">
  <svg class="crop-marks" width="732" height="1200" aria-hidden="true">
    <g stroke="var(--crop)" stroke-width="1">
      <line x1="121.5" y1="167" x2="121.5" y2="248"/>
      <line x1="623.5" y1="167" x2="623.5" y2="248"/>
      <line x1="121.5" y1="912" x2="121.5" y2="995"/>
      <line x1="623.5" y1="912" x2="623.5" y2="995"/>
      <line x1="0" y1="288.5" x2="79" y2="288.5"/>
      <line x1="664" y1="288.5" x2="732" y2="288.5"/>
      <line x1="0" y1="869.5" x2="79" y2="869.5"/>
      <line x1="664" y1="869.5" x2="732" y2="869.5"/>
    </g>
  </svg>

  <div class="volume-top">330 ml</div>
  <div class="brand">VORNELO</div>

  <div class="artwork" role="img" aria-label="Illustration: a couple embracing in a snowy forest under a rainbow-coloured northern lights arc in a starry night sky">
    <div class="artwork-title">древиц</div>
  </div>

  <div class="beer-name">Naziv Piva</div>

  <div class="vertical description">Specijalno, svetlo Ale pivo.<br>Mutno, nefiltrirano i nepasterizovano.</div>
  <div class="vertical net">Netto: 330 ml</div>
  <div class="vertical abv">5,6% Alk.</div>

  <div class="dim dim-width">0.5 cm</div>
  <div class="signature-box"><span>Mesto za<br>potpis umetnika</span></div>
  <div class="dim dim-height">1.5 cm</div>
</div>
</body>
</html>
```